The Harbourgate Clinic Stationary (Medical)

Stationery for The Harbourgate clinic
using existing logos
Please also add a green apple if possible on another corner away from the logo on some of your designs

Please take a look at www.theharbourgateclinic.com.au so you can get a feel for what The Harbourgate Clinic offers our clients.

Stationary Required: business cards, letter head, comp slips

I do not require envelopes or invoives.
Updates

Target Market(s)

The general popultation needing medical care
Professionals
Mums & Dads
Elderly

Industry/Entity Type

Business

Requirements
Must have
• Company Logo

Address
Email
Website
Phone
Should not have
• Traditional Medical Icons
No Times New Roman

```html
<!DOCTYPE html>
<html lang="en">
<head>
<meta charset="utf-8">
<title>The Harbourgate Clinic – Letterhead</title>
<link rel="stylesheet" href="https://fonts.googleapis.com/css2?family=Quicksand:wght@500;600&display=swap">
<style>
  :root {
    --sky-blue: #00aeef;
    --pale-blue: #8fd8f6;
    --leaf-green: #8dc63f;
    --soft-green: #c3dd7a;
    --pale-green: #d7e69a;
    --motif-green: #a6d15a;
    --ink-grey: #4d4d4d;
    --paper: #ffffff;
  }
  html, body {
    margin: 0;
    padding: 0;
    overflow: hidden;
    background: var(--paper);
  }
  .letterhead {
    position: relative;
    width: 848px;
    height: 1200px;
    overflow: hidden;
    background: var(--paper);
    font-family: "Quicksand", sans-serif;
  }
  .letterhead__art {
    position: absolute;
    inset: 0;
    width: 848px;
    height: 1200px;
  }
  .brand {
    position: absolute;
    left: 126px;
    top: 60px;
    display: flex;
    align-items: center;
    gap: 24px;
  }
  .brand__dot {
    flex: none;
    width: 66px;
    height: 66px;
    border-radius: 50%;
    background: var(--leaf-green);
  }
  .brand__name {
    font-size: 25px;
    font-weight: 600;
    color: var(--sky-blue);
    line-height: 1.12;
  }
  .brand__line { display: block; }
  .contact {
    position: absolute;
    left: 24px;
    bottom: 18px;
    font-size: 12.5px;
    font-weight: 500;
    color: var(--ink-grey);
  }
  .contact__address { margin: 0 0 10px; }
  .contact__row {
    display: flex;
    gap: 42px;
    align-items: center;
  }
  .contact__item {
    display: flex;
    align-items: center;
    gap: 5px;
  }
  .contact__icon { width: 14px; height: 12px; }
  .motif-area {
    position: absolute;
    left: 766px;
    top: 1096px;
    width: 44px;
    height: 48px;
    background: var(--motif-green);
  }
  .website {
    position: absolute;
    right: 26px;
    bottom: 18px;
    font-size: 15px;
    font-weight: 500;
    color: var(--paper);
    margin: 0;
  }
</style>
</head>
<body>
<div class="letterhead">
  <svg class="letterhead__art" viewBox="0 0 848 1200" aria-hidden="true">
    <path class="wave wave--pale-blue" fill="var(--pale-blue)"
      d="M0,0 H848 V118 C760,122 660,116 560,102 C420,80 300,42 190,32 C110,26 40,60 0,132 Z"/>
    <path class="wave wave--sky-blue" fill="var(--sky-blue)"
      d="M0,0 H848 V90 C740,94 620,82 480,52 C360,24 250,12 170,18 C100,24 40,48 0,76 Z"/>
    <path class="wave wave--pale-green" fill="var(--pale-green)"
      d="M0,1098 C300,1094 600,1080 848,1010 V1200 H0 Z"/>
    <path class="wave wave--soft-green" fill="var(--soft-green)"
      d="M848,1000 C800,1100 680,1160 520,1200 H848 Z"/>
    <path class="wave wave--leaf-green" fill="var(--leaf-green)"
      d="M848,975 C830,1080 760,1150 620,1200 H848 Z"/>
  </svg>

  <div class="brand">
    <span class="brand__dot"></span>
    <span class="brand__name">
      <span class="brand__line">The</span>
      <span class="brand__line">Harbourgate</span>
      <span class="brand__line">Clinic</span>
    </span>
  </div>

  <div class="motif-area" role="img" aria-label="Area for a small fruit decoration in the corner"></div>

  <div class="contact">
    <p class="contact__address">Shop 4, Brookvale Market Place 8 - 14 The Riverbend Parkway Brookvale 2100</p>
    <div class="contact__row">
      <span class="contact__item">
        <svg class="contact__icon" viewBox="0 0 14 12" aria-hidden="true">
          <path d="M3,11 C3,6 6,2 11,1" fill="none" stroke="var(--sky-blue)" stroke-width="2" stroke-linecap="round"/>
        </svg>
        02 5550 1482
      </span>
      <span class="contact__item">
        <svg class="contact__icon" viewBox="0 0 14 12" aria-hidden="true">
          <rect x="0.5" y="1.5" width="13" height="9" fill="none" stroke="var(--sky-blue)"/>
          <path d="M0.5,1.5 L7,7 L13.5,1.5" fill="none" stroke="var(--sky-blue)"/>
        </svg>
        brookvale@theharbourgateclinic.com.au
      </span>
    </div>
  </div>

  <p class="website">www.theharbourgateclinic.com.au</p>
</div>
</body>
</html>
```